Business Card for Auto Dealership - Clean, sharp and professional

Please use the maroon logo with the grey background. Need a sharp, clean and professional business card for an Auto Dealer. In the files provides there is three different logos. I have not decided which one to go with yet. Right now I am favoring the grey/silver background. I would like my contact info on there and the website as well. I feel like less is more and want something simple, clean and sharp. Thank you in advance for your tie and effort! I also need email signature, letterhead, etc after this

Target Market(s)

Car buyers

Industry/Entity Type

Automotive

Contact Information for Business Card

Drew
555-214-7730
www.BriarvaleAutoLink.example
Drew@BriarvaleAutoLink.example

Font styles to use
Serif
Sans Serif

Requirements
Must have
• Please use the maroon logo with the grey background. Business Card Details and logo from files. Please stick to the logo colors

```html
<!DOCTYPE html>
<html lang="en">
<head>
<meta charset="utf-8">
<title>Briarvale Auto Link – Business Card</title>
<link href="https://fonts.googleapis.com/css2?family=Roboto:wght@400;700&display=swap" rel="stylesheet">
<style>
  :root {
    --maroon: #4f1314;
    --maroon-text: #5a1517;
    --card-grey: #e9eaec;
    --ink: #333538;
    --faint-mark: #c6b0ae;
    --backdrop: #2c2f32;
    --white: #ffffff;
  }
  * { margin: 0; padding: 0; box-sizing: border-box; }
  html, body {
    width: 974px;
    height: 1200px;
    overflow: hidden;
    background: var(--backdrop);
    font-family: "Roboto", Arial, sans-serif;
  }
  .business-card {
    position: absolute;
    left: 0;
    top: 317px;
    width: 974px;
    height: 566px;
    background: var(--card-grey);
    overflow: hidden;
  }
  .brand-band {
    position: absolute;
    left: 0; top: 0;
    width: 100%;
    height: 243px;
    background: var(--maroon);
  }
  .brand-lockup {
    position: absolute;
    left: 86px;
    top: 74px;
    display: flex;
    align-items: center;
    gap: 26px;
  }
  .brand-dot {
    width: 96px;
    height: 96px;
    border-radius: 50%;
    border: 5px solid var(--white);
  }
  .brand-name {
    color: var(--white);
    font-weight: 700;
    font-size: 40px;
    letter-spacing: 1px;
    text-transform: uppercase;
  }
  .corner-ring {
    position: absolute;
    left: 700px;
    top: 246px;
    width: 330px;
    height: 330px;
    border-radius: 50%;
    border: 14px solid var(--faint-mark);
  }
  .contact-block {
    position: absolute;
    left: 96px;
    top: 310px;
  }
  .holder-name {
    color: var(--maroon-text);
    font-weight: 700;
    font-size: 31px;
    margin-bottom: 20px;
  }
  .contact-list { list-style: none; }
  .contact-item {
    display: flex;
    align-items: center;
    gap: 22px;
    height: 44px;
    color: var(--ink);
    font-size: 28px;
  }
  .contact-icon { width: 32px; height: 32px; flex: none; }
</style>
</head>
<body>
  <main class="business-card">
    <header class="brand-band">
      <div class="brand-lockup">
        <span class="brand-dot"></span>
        <span class="brand-name">Briarvale Auto Link</span>
      </div>
    </header>

    <div class="corner-ring" aria-hidden="true"></div>

    <section class="contact-block">
      <h1 class="holder-name">Drew</h1>
      <ul class="contact-list">
        <li class="contact-item">
          <svg class="contact-icon" viewBox="0 0 32 32" aria-hidden="true">
            <circle cx="16" cy="16" r="13" fill="none" stroke="#4f1314" stroke-width="2.5"/>
            <path d="M11 9 l3 0 1.5 4 -2 1.5 c1 2.5 2.5 4 5 5 l1.5 -2 4 1.5 0 3 c-7 1 -14 -6 -13 -13z" fill="#4f1314"/>
          </svg>
          <span>555-214-7730</span>
        </li>
        <li class="contact-item">
          <svg class="contact-icon" viewBox="0 0 32 32" aria-hidden="true">
            <circle cx="16" cy="16" r="13" fill="none" stroke="#4f1314" stroke-width="2.5"/>
            <rect x="9" y="11" width="14" height="10" fill="#4f1314"/>
            <path d="M9 11 l7 6 7 -6" fill="none" stroke="#e9eaec" stroke-width="1.5"/>
          </svg>
          <span>Drew@BriarvaleAutoLink.example</span>
        </li>
        <li class="contact-item">
          <svg class="contact-icon" viewBox="0 0 32 32" aria-hidden="true">
            <circle cx="16" cy="16" r="12" fill="none" stroke="#4f1314" stroke-width="2.5"/>
            <ellipse cx="16" cy="16" rx="5" ry="12" fill="none" stroke="#4f1314" stroke-width="2"/>
            <path d="M4 16 h24 M6 10 h20 M6 22 h20" stroke="#4f1314" stroke-width="2"/>
          </svg>
          <span>www.BriarvaleAutoLink.example</span>
        </li>
      </ul>
    </section>
  </main>
</body>
</html>
```